The Steel Hand Close Quarters Protocol Cover

Hi we are producing a self defense course entitled The Steel Hand Close Quarters Protocol: A Complete Field Manual For Commanding The Blade Every Operator Trusts Above Any Other Tool.

I listed this as a book cover but it will actually be a DVD set, but the book cover model works fine.

See below for design examples - I am thinking we need a cover that will appeal to military/survival type people.

Target Market(s)

survivalists, cops, preppers, gun owners, martial artists, and average people wanting to learn how to defend themselves

Industry/Entity Type

Defense

Requirements
Must have
• Title: THE STEEL HAND CLOSE QUARTERS PROTOCOL: A COMPLETE FIELD MANUAL FOR COMMANDING THE BLADE EVERY OPERATOR TRUSTS ABOVE ANY OTHER TOOL
Nice to have
• Please look at these sample designs from other books as a model:
• https://files.pelorvane-archive.example/covers/4/27/MarlowGrayfield.jpg - This stye is ideal.
• Other good examples:
• https://media2.quillorbit.example/8841027_k390.jpg
• http://c.tovenreads.example/titles/1289045517m/48102936.jpg
• http://img.brisketmart.example/pics/P/73Rt82MqWnB._XZ_QT410_LM305,410_.jpg
• http://3.cdn.jottlepage.example/-MRtYVVKDDQ/BWNs_harpoQ/BBBBBBBBx9K/TRPk418WpXZ/s1600/Q3408817.JPG

```html
<!DOCTYPE html>
<html lang="en">
<head>
<meta charset="utf-8">
<title>The Steel Hand Close Quarters Protocol Cover</title>
<link rel="stylesheet" href="https://fonts.googleapis.com/css2?family=Montserrat:wght@600;700;800;900&display=swap">
<style>
  :root {
    --cover-yellow: #f9e81a;
    --ink-black: #0d0d0d;
    --title-white: #ffffff;
    --label-yellow: #f9e81a;
    --scratch: rgba(20, 20, 20, 0.55);
  }
  html, body {
    margin: 0;
    padding: 0;
    width: 800px;
    height: 1200px;
    overflow: hidden;
    background: var(--cover-yellow);
  }
  .cover {
    position: relative;
    width: 800px;
    height: 1200px;
    overflow: hidden;
    background: var(--cover-yellow);
    font-family: "Montserrat", sans-serif;
  }
  .cover-shapes {
    position: absolute;
    inset: 0;
  }
  .credits {
    position: absolute;
    left: 36px;
    top: 22px;
    display: grid;
    grid-template-columns: auto auto;
    column-gap: 20px;
    row-gap: 10px;
    align-items: baseline;
  }
  .credit-label {
    color: var(--label-yellow);
    font-weight: 600;
    font-size: 20px;
  }
  .credit-value {
    color: var(--title-white);
    font-weight: 700;
    font-size: 28px;
    letter-spacing: 0.5px;
  }
  .credit-value.company { font-size: 22px; }
  .title {
    position: absolute;
    inset: 0;
    margin: 0;
    color: var(--title-white);
    font-weight: 900;
    text-transform: uppercase;
  }
  .title span { position: absolute; line-height: 1; white-space: nowrap; }
  .title-lead { left: 68px; top: 238px; font-size: 82px; letter-spacing: 1px; }
  .title-small { left: 306px; top: 252px; font-size: 24px; font-weight: 800; }
  .title-vertical {
    left: 318px;
    top: 318px;
    width: 72px;
    font-size: 74px;
    display: flex;
    flex-direction: column;
    align-items: center;
    gap: 18px;
  }
  .title-vertical b { font-weight: 900; line-height: 1; }
  .title-mid { left: 322px; top: 716px; font-size: 30px; font-weight: 800; }
  .title-main { right: 34px; top: 768px; font-size: 66px; letter-spacing: -1px; }
  .subtitle {
    position: absolute;
    left: 50px;
    top: 880px;
    width: 700px;
    margin: 0;
    color: var(--title-white);
    font-weight: 900;
    font-size: 38px;
    line-height: 52px;
    text-align: center;
    text-transform: uppercase;
    text-shadow: 2px 2px 0 var(--ink-black), -2px -2px 0 var(--ink-black),
                 2px -2px 0 var(--ink-black), -2px 2px 0 var(--ink-black);
  }
</style>
</head>
<body>
<main class="cover">
  <svg class="cover-shapes" width="800" height="1200" viewBox="0 0 800 1200" aria-hidden="true">
    <polygon class="top-band" points="0,0 800,0 800,55 0,245" fill="var(--ink-black)"/>
    <polygon class="bottom-band" points="0,1040 800,870 800,1200 0,1200" fill="var(--ink-black)"/>
    <line class="scratch-line" x1="0" y1="262" x2="800" y2="258" stroke="var(--scratch)" stroke-width="3"/>
    <line class="scratch-line" x1="0" y1="556" x2="800" y2="552" stroke="var(--scratch)" stroke-width="3"/>
    <line class="scratch-line" x1="0" y1="852" x2="800" y2="848" stroke="var(--scratch)" stroke-width="3"/>
  </svg>

  <div class="credits">
    <span class="credit-label">Author</span>
    <span class="credit-value">GARRETT L HOLLOWAY</span>
    <span class="credit-label">Company</span>
    <span class="credit-value company">IRONFIELD MOTION MEDIA</span>
  </div>

  <h1 class="title">
    <span class="title-lead">The</span>
    <span class="title-small">Steel</span>
    <span class="title-vertical"><b>H</b><b>A</b><b>N</b><b>D</b></span>
    <span class="title-mid">Close Quarters</span>
    <span class="title-main">Protocol</span>
  </h1>

  <p class="subtitle">A Complete Field Manual For Commanding The Blade Every Operator Trusts Above Any Other Tool</p>
</main>
</body>
</html>
```